Valquor.com Personal Trainer/Fitness Website

I want a website to market my personal training/Outdoor Bootcamp Class services, as well as to ditribute nutrabel. I need a logo as well I included an address for the Bramford Gales 1975 logo. I'd like Valquor in place of Bramford Gales, and in Black and white, just different enough so I can't get sued by the PBL.
https://www.lookfindr-example.net/imgview?src=http%3A%2F%2Fwww.dorian-phelkamp-example.com%2Fmedia%2Fuploads%2F2014%2F01%2Fgales_logo4.jpg&ref=http%3A%2F%2Fwww.dorian-phelkamp-example.com%2Fpbl-logo-redesigns-harbor-storm%2F&id=_kqvxx8PLRbWmNc&tb=z3wqT7KbRsJpYL%3A&w=600&h=450&client=mobile-android&bih=512&biw=360&ved=0bXYfQrTpLmVnWsKdQzHyUeRtAbCdEfGhIjKlMn&iact=mrc&uact=8.
It should be about 5 pages 1. home 2. about 3. Services 4. Blog/Videos and programs 5. Contact.
http://www.brenvoltraining.co.uk/ is a website I like the style of.

Target Market(s)

Seattle area

Industry/Entity Type

Fitness

Coding

Number of Pages Required

Font styles to use
Serif
Sans Serif

Requirements
Must have
• A minimal look
Nice to have
• A logo similar to the 1975 Bramford Galeforce Logo, with a Small Rowan Pell ripping his shirt open(with a picture of the logo on his shirt, picture within picture) to turn into Ironwing in the center. Skyline is black, Background and small figure white(with black logo on shirt)

```html
<!DOCTYPE html>
<html lang="en">
<head>
<meta charset="utf-8">
<title>Valquor – Personal Training</title>
<link rel="stylesheet" href="https://fonts.googleapis.com/css2?family=Mulish:wght@300;400;600;700&display=swap">
<style>
:root{
  --red:#c3161e;
  --ink:#222;
  --text:#555;
  --muted:#999;
  --soft:#f2f2f2;
  --line:#dcdcdc;
  --dark:#262626;
  --darker:#1f1f1f;
  --white:#fff;
}
*{box-sizing:border-box;margin:0;padding:0}
html,body{width:1200px;height:2628px;overflow:hidden}
body{position:relative;background:var(--white);font-family:"Mulish",Arial,sans-serif;color:var(--text)}
.abs{position:absolute}
.media{position:absolute;display:block}

/* header */
.site-header{position:absolute;left:0;top:0;width:1200px;height:119px;background:var(--white)}
.brand-mark{left:140px;top:14px;width:64px;height:50px;border-radius:50%;background:var(--ink)}
.brand-name{left:132px;top:60px;font-size:32px;font-weight:700;color:var(--ink);letter-spacing:-.5px}
.call{right:135px;top:26px;font-size:15px;color:var(--ink);display:flex;align-items:center;gap:6px}
.nav a{position:absolute;top:78px;font-size:12px;color:var(--ink);text-decoration:none}
.nav a.active{border-bottom:1px solid var(--ink);padding-bottom:2px}

/* hero */
.hero{left:0;top:119px;width:1200px;height:400px;background:radial-gradient(ellipse at 60% 40%,#4a4a4a 0%,#1c1c1c 55%,#050505 100%)}
.hero-figure{left:508px;top:119px;width:350px;height:400px;background:linear-gradient(180deg,#6b4a37 0%,#3d2a20 60%,#22170f 100%);opacity:.85}
.hero-title{left:137px;top:238px;font-size:31px;font-weight:700;color:var(--white)}
.hero-copy{left:137px;top:283px;width:340px;font-size:11.5px;line-height:17px;color:var(--white)}
.btn-primary{left:137px;top:352px;width:140px;height:39px;background:var(--white);color:var(--ink);font-size:13px;font-weight:600;display:flex;align-items:center;justify-content:center;border-radius:2px}
.dots{display:flex;gap:7px}
.dots i{width:9px;height:9px;border-radius:50%;display:block}
.hero-dots{left:570px;top:484px}
.hero-dots i{border:1.5px solid var(--white);background:rgba(255,255,255,.25)}

/* welcome */
.section-title{position:absolute;left:0;width:1200px;text-align:center;font-size:30px;font-weight:700;color:var(--red)}
.welcome-copy{left:133px;top:604px;width:934px;text-align:center;font-size:10.5px;line-height:19.5px;color:var(--text)}

/* services */
.band-grey{left:0;width:1200px;background:var(--soft)}
.avatar{left:535px;top:695px;width:130px;height:130px;border-radius:50%;background:radial-gradient(circle at 50% 45%,#9a7059 0%,#4a3428 60%,#1e1814 100%);border:3px solid var(--white)}
.service-img{top:922px;width:287px;height:198px}
.service-name{top:1134px;width:287px;text-align:center;font-size:18px;color:var(--ink)}

/* testimonials */
.testi-title{left:0;top:1244px;width:1200px;text-align:center;font-size:38px;font-weight:300;color:#b9b9b9}
.testi-quote{left:0;top:1304px;width:1200px;text-align:center;font-size:22px;color:#555}
.testi-quote b{color:#bdbdbd;font-size:34px;font-weight:700;vertical-align:-6px;margin:0 6px}
.testi-name{left:0;top:1346px;width:1200px;text-align:center;font-size:17px;color:var(--red)}
.testi-dots{left:558px;top:1385px;gap:14px}
.testi-dots i{background:#c4c4c4}
.testi-dots i.on{background:var(--red)}

/* blog */
.blog-title{left:131px;top:1476px;font-size:38px;color:var(--red)}
.pager{top:1486px;width:23px;height:28px;border:1px solid var(--line);background:var(--white);display:flex;align-items:center;justify-content:center}
.post-img{top:1547px;width:274px;height:173px}
.date-badge{width:40px;height:44px;background:rgba(30,30,30,.85);color:var(--white);text-align:center;font-size:18px;line-height:20px;padding-top:4px}
.date-badge small{display:block;font-size:9px;line-height:10px}
.post-head{top:1734px;width:274px;font-size:13px;font-weight:700;line-height:17px;color:var(--ink)}
.post-body{top:1776px;width:274px;font-size:9.6px;line-height:16px;color:var(--muted);text-align:justify}

/* classes & contact */
.class-img{top:1969px;width:288px;height:168px}
.class-title{top:2150px;font-size:23px;color:var(--red)}
.class-copy{top:2182px;width:288px;font-size:10px;line-height:17px;color:var(--muted)}
.btn-ghost{top:2249px;width:71px;height:29px;background:#e4e4e4;color:#777;font-size:10px;display:flex;align-items:center;justify-content:center}
.contact-title{left:767px;top:1962px;font-size:23px;color:var(--red)}
.field{border:1px solid var(--line);background:var(--white);font-size:9.5px;color:#aaa;padding:10px 12px}
.btn-dark{left:767px;top:2249px;width:57px;height:29px;background:#2a2a2a;color:var(--white);font-size:10px;display:flex;align-items:center;justify-content:center}

/* footer */
.site-footer{left:0;top:2340px;width:1200px;height:218px;background:var(--dark)}
.footer-bar{left:0;top:2558px;width:1200px;height:70px;background:var(--darker)}
.foot-title{top:2378px;font-size:19px;color:var(--white);font-weight:400}
.foot-rule{left:133px;top:2411px;width:196px;height:1px;background:#444}
.foot-list{list-style:none;font-size:10.5px;line-height:21px;color:#cfcfcf}
.foot-list li::before{content:"•";margin-right:7px;color:#aaa}
.info-row{left:382px;display:flex;align-items:center;gap:10px;color:#cfcfcf}
.map{left:652px;top:2428px;width:166px;height:93px;background:linear-gradient(135deg,#e9e9e6,#d6d8d4);border:1px solid #555}
.social{width:23px;height:23px;border-radius:2px}
.copyright{left:133px;top:2584px;font-size:10px;color:#bbb}
.to-top{left:1042px;top:2578px}
</style>
</head>
<body>

<header class="site-header">
  <div class="abs brand-mark"></div>
  <div class="abs brand-name">Valquor</div>
  <div class="abs call">
    <svg width="13" height="13" viewBox="0 0 24 24"><path fill="#222" d="M6.6 10.8a15.1 15.1 0 0 0 6.6 6.6l2.2-2.2a1 1 0 0 1 1-.25 11.4 11.4 0 0 0 3.6.57 1 1 0 0 1 1 1V20a1 1 0 0 1-1 1A17 17 0 0 1 3 4a1 1 0 0 1 1-1h3.5a1 1 0 0 1 1 1c0 1.25.2 2.45.57 3.57a1 1 0 0 1-.25 1z"/></svg>
    Call us on : 555 014 2287
  </div>
  <nav class="nav">
    <a class="active" style="left:687px">Home</a>
    <a style="left:753px">About</a>
    <a style="left:818px">Services</a>
    <a style="left:895px">Blog</a>
    <a style="left:951px">Videos</a>
    <a style="left:1021px">Contact</a>
  </nav>
</header>

<section>
  <div class="media hero" role="img" aria-label="Dark studio backdrop"></div>
  <div class="media hero-figure" role="img" aria-label="Athlete seen from behind lifting a dumbbell overhead"></div>
  <h1 class="abs hero-title">Aenean vitae maximus</h1>
  <p class="abs hero-copy">Maecenas faucibus arcu vitae velit rutrum, maximus dictum orci mattis. Nulla euismod lacus ornare lobortis. Aliquam lacinia tortor neque, id dapibus sem tempus.</p>
  <div class="abs btn-primary">Get Started Now</div>
  <div class="abs dots hero-dots"><i></i><i></i><i></i><i></i></div>
</section>

<section>
  <h2 class="section-title" style="top:554px">Welcome to Valquor</h2>
  <p class="abs welcome-copy">Morbi vestibulum enim eget justo ultrices, condimentum auctor nunc luctus. Morbi eget venenatis turpis. Nam egestas, ipsum ac rutrum imperdiet, sapien odio scelerisque orci, ac tincidunt ex eros nec urna. Nulla viverra leo enim, at tristique nulla porttitor nec. Phasellus semper dui non lectus tristique, quis finibus risus blandit. Fusce sollicitudin nisi ac placerat fringilla. Duis quis est arcu. Vestibulum malesuada mi non dui lobortis, non semper tortor tristique. Pellentesque habitant morbi tristique senectus et netus et malesuada fames ac turpis egestas. Sed rutrum enim nec mollis congue. Aenean vitae lectus maximus, lobortis lectus eget, aliquam nisi.</p>
</section>

<section>
  <div class="abs band-grey" style="top:757px;height:448px"></div>
  <div class="media avatar" role="img" aria-label="Portrait of the personal trainer"></div>
  <h2 class="section-title" style="top:853px">Our Services</h2>
  <div class="media service-img" style="left:133px;background:linear-gradient(135deg,#5a5550,#2b2826)" role="img" aria-label="Trainer guiding a client with dumbbells"></div>
  <div class="media service-img" style="left:456px;background:linear-gradient(135deg,#8a8f96,#3c4046)" role="img" aria-label="Man doing a push-up in a gym"></div>
  <div class="media service-img" style="left:780px;background:linear-gradient(180deg,#a9b29a,#5d7a3e)" role="img" aria-label="Group holding planks on grass outdoors"></div>
  <div class="abs service-name" style="left:133px">Personal Training</div>
  <div class="abs service-name" style="left:456px">Fitness</div>
  <div class="abs service-name" style="left:780px">Outdoor Bootcamp Class</div>
</section>

<section>
  <h2 class="abs testi-title">Client’s Testimonials</h2>
  <p class="abs testi-quote"><b>“</b>Donec sapien est, feugiat id magna at, tristique erat. Etiam fringilla augue leo.<b>”</b></p>
  <p class="abs testi-name">Jon Marlow, City</p>
  <div class="abs dots testi-dots"><i class="on"></i><i></i><i></i><i></i></div>
</section>

<section>
  <div class="abs band-grey" style="top:1442px;height:455px"></div>
  <h2 class="abs blog-title">Blog</h2>
  <div class="abs pager" style="left:1018px"><svg width="8" height="12" viewBox="0 0 8 12"><path d="M6 1 1 6l5 5" fill="none" stroke="#999" stroke-width="1.5"/></svg></div>
  <div class="abs pager" style="left:1042px"><svg width="8" height="12" viewBox="0 0 8 12"><path d="m2 1 5 5-5 5" fill="none" stroke="#999" stroke-width="1.5"/></svg></div>

  <div class="media post-img" style="left:133px;background:linear-gradient(135deg,#8c8c8c,#2e2e2e)" role="img" aria-label="Two athletes training on the floor"></div>
  <div class="media post-img" style="left:462px;background:linear-gradient(135deg,#c9c3bd,#6f5d63)" role="img" aria-label="Step aerobics class"></div>
  <div class="media post-img" style="left:792px;background:linear-gradient(135deg,#eceae6,#9ea4a8)" role="img" aria-label="Couple jogging outdoors"></div>
  <div class="abs date-badge" style="left:133px;top:1676px">06<small>MAY</small></div>
  <div class="abs date-badge" style="left:462px;top:1676px">06<small>MAY</small></div>
  <div class="abs date-badge" style="left:792px;top:1676px">06<small>MAY</small></div>

  <h3 class="abs post-head" style="left:133px">Duis a nisi rhoncus, porta diam a, ornare eros. Fusce et enim lobortis, lacinia nisl at</h3>
  <h3 class="abs post-head" style="left:462px">Duis a nisi rhoncus, porta diam a, ornare eros. Fusce et enim lobortis, lacinia nisl at</h3>
  <h3 class="abs post-head" style="left:792px">Duis a nisi rhoncus, porta diam a, ornare eros. Fusce et enim lobortis, lacinia nisl at</h3>
  <p class="abs post-body" style="left:133px">Aliquam in augue sit amet justo tincidunt malesuada. Etiam nec ante massa. In nec fermentum est, non commodo sem. Pellentesque id eros est. Pellentesque molestie ut lacus pellentesque venenatis.</p>
  <p class="abs post-body" style="left:462px">Aliquam in augue sit amet justo tincidunt malesuada. Etiam nec ante massa. In nec fermentum est, non commodo sem. Pellentesque id eros est. Pellentesque molestie ut lacus pellentesque venenatis.</p>
  <p class="abs post-body" style="left:792px">Aliquam in augue sit amet justo tincidunt malesuada. Etiam nec ante massa. In nec fermentum est, non commodo sem. Pellentesque id eros est. Pellentesque molestie ut lacus pellentesque venenatis.</p>
</section>

<section>
  <div class="media class-img" style="left:133px;background:linear-gradient(135deg,#2d4f86,#0f1c36)" role="img" aria-label="Man training with dumbbells under blue light"></div>
  <div class="media class-img" style="left:450px;background:linear-gradient(135deg,#6a6a6a,#1d1d1d)" role="img" aria-label="Woman in a step class"></div>
  <h3 class="abs class-title" style="left:133px;font-weight:400">Class#1</h3>
  <h3 class="abs class-title" style="left:450px;font-weight:400">Class#2</h3>
  <p class="abs class-copy" style="left:133px">Either you need Dallas/Ft. Worth Office Space, Dallas Executive Suites, Ft. Worth Executive Suites, Houston Office Space, Houston Executive Suites, or maybe you simply need…</p>
  <p class="abs class-copy" style="left:450px">Either you need Dallas/Ft. Worth Office Space, Dallas Executive Suites, Ft. Worth Executive Suites, Houston Office Space, Houston Executive Suites, or maybe you simply need…</p>
  <div class="abs btn-ghost" style="left:133px">Read more</div>
  <div class="abs btn-ghost" style="left:450px">Read more</div>

  <h3 class="abs contact-title" style="font-weight:400">Contact us</h3>
  <div class="abs field" style="left:767px;top:2003px;width:144px;height:33px">Name</div>
  <div class="abs field" style="left:922px;top:2003px;width:143px;height:33px">City</div>
  <div class="abs field" style="left:767px;top:2048px;width:144px;height:33px">Phone</div>
  <div class="abs field" style="left:922px;top:2048px;width:143px;height:33px">Email</div>
  <div class="abs field" style="left:767px;top:2092px;width:298px;height:139px;padding-top:20px">Message</div>
  <div class="abs btn-dark">Submit</div>
</section>

<footer>
  <div class="abs site-footer"></div>
  <div class="abs footer-bar"></div>

  <h4 class="abs foot-title" style="left:133px">Quick Links</h4>
  <div class="abs foot-rule"></div>
  <ul class="abs foot-list" style="left:133px;top:2424px"><li>Home</li><li>About</li><li>Services</li><li>Blog</li><li>Videos</li></ul>
  <ul class="abs foot-list" style="left:231px;top:2424px"><li>Contact</li><li>Sitemap</li></ul>

  <h4 class="abs foot-title" style="left:382px">Contact info</h4>
  <div class="abs info-row" style="top:2427px;font-size:10px">
    <svg width="10" height="12" viewBox="0 0 10 14"><path d="M5 0a5 5 0 0 0-5 5c0 3.8 5 9 5 9s5-5.2 5-9a5 5 0 0 0-5-5zm0 7a2 2 0 1 1 0-4 2 2 0 0 1 0 4z" fill="#aaa"/></svg>
    24 Building name, Street name, City - Zipcode
  </div>
  <div class="abs info-row" style="top:2450px;font-size:15px">
    <svg width="11" height="11" viewBox="0 0 24 24"><path fill="#aaa" d="M6.6 10.8a15.1 15.1 0 0 0 6.6 6.6l2.2-2.2a1 1 0 0 1 1-.25 11.4 11.4 0 0 0 3.6.57 1 1 0 0 1 1 1V20a1 1 0 0 1-1 1A17 17 0 0 1 3 4a1 1 0 0 1 1-1h3.5a1 1 0 0 1 1 1c0 1.25.2 2.45.57 3.57a1 1 0 0 1-.25 1z"/></svg>
    555.014.2290
  </div>
  <div class="abs info-row" style="top:2478px;font-size:15px">
    <svg width="11" height="9" viewBox="0 0 12 9"><rect width="12" height="9" fill="#aaa"/><path d="M0 0l6 5 6-5" fill="none" stroke="#262626" stroke-width="1.2"/></svg>
    info@valquor.com
  </div>
  <div class="media map" role="img" aria-label="Location map"></div>

  <h4 class="abs foot-title" style="left:860px">Share us on</h4>
  <div class="abs social" style="left:862px;top:2429px;background:#3b5b9a"></div>
  <div class="abs social" style="left:909px;top:2429px;background:#3aa6dc"></div>
  <div class="abs social" style="left:953px;top:2429px;background:#1d72a8"></div>
  <div class="abs social" style="left:999px;top:2429px;background:#b0b0b0"></div>
  <div class="abs social" style="left:1044px;top:2429px;background:#d8332a"></div>
  <div class="abs social" style="left:862px;top:2472px;background:#e6e6e6"></div>

  <p class="abs copyright">Copyright &copy; 2016 Valquor. &nbsp;All rights reserved.</p>
  <svg class="abs to-top" width="26" height="26" viewBox="0 0 26 26"><circle cx="13" cy="13" r="12" fill="none" stroke="#888" stroke-width="1.2"/><path d="M13 18V8M9 12l4-4 4 4" fill="none" stroke="#888" stroke-width="1.4"/></svg>
</footer>

</body>
</html>
```